Junior Rugby Event needs 4 page Brochure

4 Page A4 brochure to be designed for a junior rugby event to be held in japan.. The brochure will entice coaches, teachers and players to the event.
The brochure will provide a basic overview of the event - dates, venue and promote some of the key features of the host, venue and event.
Event logo has been included. Design overview with copy has been included as word document. Images have been attached that can be used or alternatives sourced. A PDF document has been included of a design example that we like.
Rugby Clubs and Schools
Events

```html
<!DOCTYPE html>
<html lang="en">
<head>
<meta charset="utf-8">
<title>Travel &amp; Tournament Package</title>
<link href="https://fonts.googleapis.com/css2?family=Lato:wght@400;700&family=Lobster&family=Montserrat:wght@400;600&display=swap" rel="stylesheet">
<style>
  :root {
    --bg: #efe7dc;
    --paper: #ffffff;
    --red: #d7282f;
    --navy: #262f5e;
    --ink: #2a2f5a;
    --sky: #bcd8f0;
    --maple: #b3202c;
    --maple-dark: #6e1420;
    --snow: #f4f7fb;
    --forest: #4c7a4e;
  }
  * { margin: 0; padding: 0; box-sizing: border-box; }
  html, body { width: 1200px; height: 1200px; overflow: hidden; background: var(--bg); }
  .page {
    position: absolute; left: 190px; top: 20px;
    width: 820px; height: 1160px;
    background: var(--paper);
    box-shadow: 0 4px 18px rgba(0,0,0,0.18);
    overflow: hidden;
  }
  .hero {
    position: absolute; left: 0; top: 0; width: 820px; height: 857px;
    background:
      linear-gradient(180deg, rgba(110,20,32,0.85) 0%, rgba(179,32,44,0.55) 9%, rgba(179,32,44,0.18) 17%, rgba(179,32,44,0) 24%),
      linear-gradient(90deg, rgba(150,24,36,0.75) 0%, rgba(179,32,44,0.25) 10%, rgba(179,32,44,0) 18%, rgba(179,32,44,0) 84%, rgba(179,32,44,0.3) 92%, rgba(150,24,36,0.7) 100%),
      linear-gradient(180deg, #c3dcf1 0%, var(--sky) 20%, #dce9f5 36%, #eef3f9 46%, #ffffff 56%);
  }
  .hero-peak {
    position: absolute; left: 0; top: 0; width: 820px; height: 857px;
    background: linear-gradient(180deg, rgba(244,247,251,0) 30%, rgba(214,226,240,0.75) 38%, rgba(244,247,251,0.9) 46%, rgba(255,255,255,0) 56%);
    -webkit-mask-image: linear-gradient(90deg, transparent 8%, #000 30%, #000 58%, transparent 80%);
            mask-image: linear-gradient(90deg, transparent 8%, #000 30%, #000 58%, transparent 80%);
  }
  .photo { position: absolute; }
  .photo-arena { left: 0; top: 374px; width: 410px; height: 196px; background: linear-gradient(180deg, #3f6b44 0%, var(--forest) 70%, #6aa04a 100%); }
  .photo-city { left: 0; top: 578px; width: 201px; height: 248px; background: linear-gradient(160deg, #1b1d4a 0%, #b02b3a 50%, #e0a53a 100%); }
  .photo-shrine { left: 208px; top: 578px; width: 202px; height: 248px; background: linear-gradient(180deg, #c9d4df 0%, #d2402c 45%, #9a9a98 100%); }
  .content {
    position: absolute; left: 438px; top: 0; width: 320px;
    font-family: "Lato", sans-serif; font-size: 14.4px; line-height: 16.7px; color: var(--ink);
  }
  .title { position: absolute; left: 0; top: 298px; white-space: nowrap; font-family: "Lobster", cursive; font-weight: 400; color: var(--red); font-size: 24px; line-height: 30px; }
  .intro { position: absolute; left: 0; top: 336px; width: 320px; }
  .package { position: absolute; left: 0; width: 320px; }
  .package-player { top: 446px; }
  .package-supporter { top: 646px; }
  .package-title { color: var(--red); font-weight: 700; font-size: 14.4px; line-height: 16.7px; }
  .package-list { list-style: none; }
  .package-list li { position: relative; padding-left: 20px; width: 322px; }
  .package-list li::before { content: "•"; position: absolute; left: 0; }
  .band-red { position: absolute; left: 0; top: 857px; width: 820px; height: 13px; background: var(--red); }
  .band-navy { position: absolute; left: 0; top: 870px; width: 820px; height: 290px; background: var(--navy); color: #fff; font-family: "Montserrat", sans-serif; text-align: center; }
  .cta { position: absolute; left: 0; right: 0; top: 104px; font-size: 18.6px; line-height: 20px; letter-spacing: 0.4px; }
  .email { position: absolute; left: 0; right: 0; top: 162px; font-size: 19px; font-weight: 600; letter-spacing: 0.3px; }
</style>
</head>
<body>
  <div class="page">
    <div class="hero" role="img" aria-label="Red maple leaves framing a snow-capped mountain under a blue sky">
      <div class="hero-peak"></div>
    </div>
    <div class="photo photo-arena" role="img" aria-label="Green sports arena building with its name on the facade"></div>
    <div class="photo photo-city" role="img" aria-label="Neon signs of a Japanese city street at night"></div>
    <div class="photo photo-shrine" role="img" aria-label="Red shrine gate building at the top of stone steps"></div>

    <div class="content">
      <h1 class="title">Travel &amp; Tournament Package</h1>
      <p class="intro">Our aim is to make participation in the Pacific Youth Rugby Cup as simple as possible for you, we therefore a number of different tournament packages. We also have a network of agents around the world who will assist you with flights and tour extension options.</p>

      <section class="package package-player">
        <h2 class="package-title">Seaside Arena Player Package</h2>
        <ul class="package-list">
          <li>6 nights accommodation in Seaside Arena Lodges, bunk rooms.</li>
          <li>Breakfast, Lunch and Dinner each day</li>
          <li>Airport or Train Station Transfers - one per team for arrival and departure.</li>
          <li>Tournament Entry (4 games guaranteed)</li>
          <li>Half Day Guided Fukuoka Sightseeing Tour including Kushida Shrine and Fukuoka Castle</li>
          <li>Exclusive Pacific Youth Rugby Cup Merchandise</li>
        </ul>
      </section>

      <section class="package package-supporter">
        <h2 class="package-title">Fukuoka Player or Supporter Package</h2>
        <ul class="package-list">
          <li>6 nights hotel accommodation in Fukuoka City.</li>
          <li>Breakfast daily</li>
          <li>Airport or Train Station Transfers - one per team for arrival and departure.</li>
          <li>Tournament Return Shuttle Service</li>
          <li>Tournament Entry (4 games guaranteed)</li>
          <li>Half Day Guided Fukuoka Sightseeing Tour including Kushida Shrine and Fukuoka Castle</li>
          <li>Exclusive Pacific Youth Rugby Cup Merchandise</li>
        </ul>
      </section>
    </div>

    <div class="band-red"></div>
    <div class="band-navy">
      <p class="cta">Please contact us to receive a tailored quote for your team<br>for the Pacific Youth Rugby Cup.</p>
      <p class="email">Info@pacificyouthrugbycup.com</p>
    </div>
  </div>
</body>
</html>
```